ALL TEXT GRAPHICS TM May 2025 for Instagram

We are looking for a series of social media graphics for Instagram (new size: 4:5 (1080 x 1350 pixels) ratio that are ALL TEXT. We want the following quotes below on each graphic; one quote per graphic. AND, In very small letters at the bottom of each graphic, add @TovaMarshOnline
The look and feel of these graphics should be complimentary to the color palette attached below; but keep them simple. But the design is up to you; at the end of this document, I provided various samples of all text graphics that I like as examples.
Target Market(s)
women looking to lose weight
Look and feel

```html
<!DOCTYPE html>
<html lang="en">
<head>
<meta charset="UTF-8">
<title>Flat Tummy in Your 40s</title>
<link href="https://fonts.googleapis.com/css2?family=Bebas+Neue&family=Figtree:wght@400;600&family=Great+Vibes&display=swap" rel="stylesheet">
<style>
  :root {
    --bg: #ffffff;
    --pink: #ff0a8a;
    --magenta: #cf0469;
    --ink: #111111;
  }
  html, body {
    margin: 0;
    padding: 0;
    overflow: hidden;
    background: var(--bg);
  }
  .post {
    position: relative;
    width: 960px;
    height: 1200px;
    background: var(--bg);
    overflow: hidden;
  }
  .accent-rule {
    position: absolute;
    left: 180px;
    top: 242px;
    width: 8px;
    height: 716px;
    background: var(--magenta);
  }
  .headline {
    position: absolute;
    left: 232px;
    top: 228px;
    margin: 0;
    font-family: "Bebas Neue", "Oswald", sans-serif;
    font-weight: 400;
    font-size: 103px;
    line-height: 104px;
    letter-spacing: 0;
  }
  .headline .line-one { display: block; color: var(--pink); }
  .headline .line-two { display: block; color: var(--magenta); }
  .subline, .offer {
    position: absolute;
    left: 232px;
    margin: 0;
    font-family: "Figtree", "Helvetica Neue", sans-serif;
    font-weight: 400;
    font-size: 43px;
    line-height: 45px;
    color: var(--ink);
  }
  .subline { top: 435px; }
  .cta-script {
    position: absolute;
    left: 230px;
    top: 575px;
    margin: 0;
    font-family: "Great Vibes", cursive;
    font-size: 120px;
    line-height: 130px;
    color: var(--magenta);
  }
  .keyword {
    position: absolute;
    left: 232px;
    top: 706px;
    margin: 0;
    font-family: "Bebas Neue", "Oswald", sans-serif;
    font-size: 103px;
    line-height: 104px;
    color: var(--pink);
  }
  .offer { top: 823px; }
  .handle {
    position: absolute;
    left: 232px;
    top: 1020px;
    margin: 0;
    font-family: "Figtree", "Helvetica Neue", sans-serif;
    font-weight: 600;
    font-size: 16px;
    color: var(--ink);
  }
</style>
</head>
<body>
  <main class="post">
    <div class="accent-rule"></div>
    <h1 class="headline">
      <span class="line-one">Flat Tummy</span>
      <span class="line-two">In Your 40s?</span>
    </h1>
    <p class="subline">It’s still<br>possible!</p>
    <p class="cta-script">Comment</p>
    <p class="keyword">BYE BELLY</p>
    <p class="offer">to get the<br>10 secrets to a<br>flatter tummy</p>
    <p class="handle">@TovaMarshOnline</p>
  </main>
</body>
</html>
```